"Drink Champagne and Dance on the Table" sort of business card needed!

We throw events, weddings, engagement parties, baby showers and the sort of end of year corporate events that people remember long after the glitter has settled - the sort of events that make you stand still and say wow when you walk in and then make you want to "Drink Champagne and Dance on the Tables"

We have a great logo with heaps of potential and need a business card that just screams creative professionals!

We are based in Auckland, NZ and are priced at the Premium end of the market were there are around 10 other main competitors. We need to stand out and make a strong statement about who we are!

Our Business Card will be one of the few items that we print out so are fully prepared to invest in a premium print job.

We really love our logo and think it has heaps of potential! Its ok if you would like to manipulate it (maybe put it on an angle, or use the circle element on its own?).

Black and Gold is very striking, but its very done in our market so we would like to avoid a solid black background please

We have done a bit of an inspiration document to give you an idea of the sort of look and feel we are hoping to achieve.

Target Market(s)

Woman aged 30 - 45 with an income bracket of $70k +

Industry/Entity Type

Event Planning

Contact Information for Business Card

Marnie
hello@fennoriwick.co.nz
www.fennoriwick.co.nz
02734419027

Number of Pages Required

5+ page

Requirements
Must have
• Vibrant colours and design (we love the vibrant pink and gold in the inspiration file)
• We would love to see some colour and creativity (although the black and gold is very striking). Because we are doing such minimal print work I am happy for the cards to be a little more expensive so if you want to use cut outs, rounded corners, gold foil, non standard size etc I am happy for that too. I really want the wow factor.
Nice to have
• We would like the design to be double sided.
Should not have
• The logo colour changed
• Use of Purple or Green or solid black background.
• Wedding Photos!

```html
<!DOCTYPE html>
<html lang="en">
<head>
<meta charset="utf-8">
<title>Fenno and Riwick — Business Card</title>
<link href="https://fonts.googleapis.com/css2?family=PT+Sans:wght@400;700&family=PT+Sans+Narrow:wght@700&display=swap" rel="stylesheet">
<style>
  :root {
    --gold: #c9a03c;
    --ink: #1f1f1f;
    --card: #ffffff;
    --backdrop: #ece9e6;
    --rule: #e3d3a8;
  }
  * { margin: 0; padding: 0; box-sizing: border-box; }
  html, body { width: 1200px; height: 900px; overflow: hidden; }
  body {
    background: var(--backdrop);
    font-family: "PT Sans", Arial, sans-serif;
    position: relative;
  }
  .card {
    position: absolute;
    background: var(--card);
    border-radius: 16px;
    box-shadow: 0 6px 20px rgba(0,0,0,0.12);
    overflow: hidden;
  }
  .brand-name {
    font-family: "PT Sans Narrow", "Arial Narrow", sans-serif;
    font-weight: 700;
    color: var(--gold);
    line-height: 1;
  }
  .tagline {
    display: flex;
    align-items: center;
    justify-content: center;
    gap: 8px;
    color: var(--gold);
    font-size: 12px;
    letter-spacing: 3px;
  }
  .tagline::before, .tagline::after {
    content: ""; width: 22px; height: 1.5px; background: var(--gold);
  }

  /* Contact side */
  .card--contact { left: 78px; top: 35px; width: 587px; height: 362px; }
  .brand-vertical {
    position: absolute;
    left: 114px; top: 180px;
    transform: translate(-50%, -50%) rotate(-90deg);
    white-space: nowrap;
    text-align: center;
  }
  .brand-vertical .brand-name { display: block; font-size: 40px; }
  .brand-vertical .tagline { margin-top: 5px; font-size: 11px; }
  .brand-vertical .tagline::before, .brand-vertical .tagline::after { width: 18px; }
  .person-name {
    position: absolute;
    left: 278px; top: 126px;
    font-size: 21px;
    font-weight: 700;
    color: var(--gold);
  }
  .contact-list {
    position: absolute;
    left: 280px; top: 178px;
    list-style: none;
  }
  .contact-list li {
    display: flex; align-items: center; gap: 8px;
    font-size: 16px; color: var(--ink);
    height: 24.5px;
  }
  .contact-list svg { width: 12px; height: 12px; flex: none; }

  /* Logo side */
  .card--logo { left: 390px; top: 506px; width: 563px; height: 349px; }
  .brand-mark {
    position: absolute;
    left: 201px; top: 34px;
    width: 160px; height: 160px;
    border: 3px solid var(--gold);
    border-radius: 50%;
  }
  .brand-stack {
    position: absolute;
    left: 0; right: 0; top: 204px;
    text-align: center;
  }
  .brand-stack .brand-name { font-size: 44px; }
  .brand-stack .tagline { font-size: 13px; margin-top: 6px; }
  .brand-stack .tagline::before, .brand-stack .tagline::after { width: 24px; }
  .web-rule {
    position: absolute;
    left: 0; right: 0; top: 290px;
    display: flex; align-items: center; gap: 14px;
  }
  .web-rule::before, .web-rule::after {
    content: ""; flex: 1; height: 1px; background: var(--rule);
  }
  .web-rule span { font-size: 15px; font-weight: 700; color: var(--ink); }
</style>
</head>
<body>
  <section class="card card--contact">
    <div class="brand-vertical">
      <span class="brand-name">Fenno and Riwick</span>
      <span class="tagline">WEDDINGS&amp;EVENTS</span>
    </div>
    <h1 class="person-name">Marnie</h1>
    <ul class="contact-list">
      <li>
        <svg viewBox="0 0 12 12"><path fill="#c9a03c" d="M2.5 0.8l2 2.2-1 1.3c.7 1.5 1.8 2.6 3.3 3.3l1.3-1 2.2 2-1.2 2C5 10.3 1.6 7 .6 2z"/></svg>
        02734419027
      </li>
      <li>
        <svg viewBox="0 0 12 12"><rect x="0.5" y="2" width="11" height="8" fill="#c9a03c"/><path d="M1 2.6l5 3.8 5-3.8" fill="none" stroke="#fff" stroke-width="1"/></svg>
        hello@fennoriwick.co.nz
      </li>
      <li>
        <svg viewBox="0 0 12 12"><g fill="none" stroke="#c9a03c" stroke-width="1.4"><rect x="0.8" y="5.5" width="6" height="3.4" rx="1.7" transform="rotate(-45 3.8 7.2)"/><rect x="5.2" y="3.1" width="6" height="3.4" rx="1.7" transform="rotate(-45 8.2 4.8)"/></g></svg>
        www.fennoriwick.co.nz
      </li>
    </ul>
  </section>

  <section class="card card--logo">
    <div class="brand-mark"></div>
    <div class="brand-stack">
      <div class="brand-name">Fenno and Riwick</div>
      <div class="tagline">WEDDINGS&amp;EVENTS</div>
    </div>
    <div class="web-rule"><span>www.fennoriwick.co.nz</span></div>
  </section>
</body>
</html>
```